law firm business cards

I need a business card using my existing logo. Two sided is best because there is a lot of information that needs to go on the card. Use the same general color scheme as logo, but I need one set with the blue background of my website (www.halvorsenlawgrp.com), and one set with white background (to see which one I like best).

Information that must be on there:
Trevor J. Halvorsen
Board Certified Civil Trial Specialist
738 Brinkley Ave., Suite 640
Raleigh, NC 27601

T 919-555-0143
F 919-555-0176

www.halvorsenlawgrp.com
trevor@halvorsenlawgrp.com

Personal Injury | Criminal Law (to separate the two, pls use a bullet point or pipeline symbol "|"

If there is a way to work in the CPRS logo (maybe at the bottom somewhere), put it in, but don't let it detract from the main logo too much.

Also, if there is a way to work it in, put in somewhere: Former Insurance Company Attorney | Former Criminal Prosecutor (to separate the two, pls use a bullet point or pipeline symbol "|"

```html
<!DOCTYPE html>
<html lang="en">
<head>
<meta charset="utf-8">
<title>Halvorsen Law – Business Cards</title>
<link rel="stylesheet" href="https://fonts.googleapis.com/css2?family=Libre+Baskerville:wght@400;700&family=Open+Sans:wght@400;600&display=swap">
<style>
  :root {
    --navy: #1c3765;
    --navy-deep: #152b52;
    --red: #d8283d;
    --paper: #ffffff;
    --stage: #e9ebef;
    --ink: #1a1d24;
    --serif: "Libre Baskerville", Georgia, serif;
    --sans: "Open Sans", Arial, sans-serif;
  }
  * { box-sizing: border-box; margin: 0; padding: 0; }
  html, body { width: 1200px; height: 987px; overflow: hidden; }
  body { background: var(--stage); font-family: var(--sans); position: relative; }

  .card {
    position: absolute;
    left: 250px;
    width: 700px;
    height: 400px;
    border-radius: 24px;
    overflow: hidden;
    box-shadow: 0 6px 18px rgba(20, 30, 50, .18);
  }
  .card--front { top: 50px; background: var(--paper); }
  .card--back { top: 537px; background: var(--navy); color: var(--paper); }

  .card__art { position: absolute; inset: 0; width: 100%; height: 100%; }

  .brand {
    position: absolute;
    display: flex;
    align-items: center;
    gap: 16px;
  }
  .brand__mark {
    width: 48px; height: 48px;
    border-radius: 50%;
    border: 5px solid currentColor;
    flex: none;
  }
  .brand__name {
    font-family: var(--serif);
    font-weight: 400;
    letter-spacing: 1px;
    text-transform: uppercase;
    line-height: 1;
  }
  .card--front .brand { left: 38px; top: 30px; color: var(--navy); }
  .card--front .brand__name { font-size: 44px; }

  .address {
    position: absolute;
    left: 40px; top: 136px;
    font-size: 17px;
    color: var(--ink);
  }
  .contact-list {
    position: absolute;
    left: 40px; top: 168px;
    list-style: none;
    font-size: 15px;
    color: var(--ink);
    line-height: 23px;
  }
  .contact-list li { display: flex; align-items: center; gap: 7px; }
  .contact-list svg { width: 13px; height: 13px; fill: var(--navy); flex: none; }

  .badge {
    position: absolute;
    left: 566px; top: 196px;
    width: 72px; height: 72px;
    border-radius: 50%;
    background: var(--paper);
    border: 3px solid var(--navy);
    box-shadow: inset 0 0 0 6px var(--paper), inset 0 0 0 8px var(--navy);
  }

  .signature {
    position: absolute;
    right: 34px; bottom: 18px;
    text-align: right;
    color: var(--paper);
  }
  .signature__name { font-family: var(--serif); font-weight: 700; font-size: 25px; line-height: 1.3; }
  .signature__title { font-size: 17px; margin-top: 2px; }

  .card--back .brand {
    left: 0; right: 0; top: 110px;
    justify-content: center;
    color: var(--paper);
  }
  .card--back .brand__mark { width: 60px; height: 60px; border-width: 6px; }
  .card--back .brand__name { font-size: 46px; }

  .practice {
    position: absolute;
    left: 0; right: 0; top: 250px;
    text-align: center;
    font-size: 19px;
    line-height: 32px;
  }
</style>
</head>
<body>

  <section class="card card--front" aria-label="Business card, white side">
    <svg class="card__art" viewBox="0 0 700 400" aria-hidden="true">
      <path d="M40 100 C240 88 470 110 640 160" fill="none" stroke="var(--red)" stroke-width="3"/>
      <path d="M0 280 C200 280 420 296 700 288" fill="none" stroke="var(--red)" stroke-width="1.5"/>
      <path d="M0 288 C200 288 420 304 700 296 L700 400 L0 400 Z" fill="var(--navy)"/>
      <path d="M0 298 C200 298 420 314 700 306" fill="none" stroke="var(--paper)" stroke-width="3"/>
      <path d="M0 332 C120 332 240 360 300 400 L0 400 Z" fill="var(--navy-deep)"/>
    </svg>

    <div class="brand">
      <span class="brand__mark"></span>
      <span class="brand__name">Halvorsen Law</span>
    </div>

    <p class="address">738 Brinkley Ave., Suite 640, Raleigh, NC 27601</p>

    <ul class="contact-list">
      <li><svg viewBox="0 0 16 16"><path d="M3 1h3l1.5 4-2 1.5a9 9 0 0 0 4 4L11 8.5l4 1.5v3a2 2 0 0 1-2 2A12 12 0 0 1 1 3a2 2 0 0 1 2-2z"/></svg>919-555-0143</li>
      <li><svg viewBox="0 0 16 16"><path d="M4 1h7v4H4zM1 6h14v7h-3v2H4v-2H1zM5 10v4h6v-4z"/></svg>919-555-0176</li>
      <li><svg viewBox="0 0 16 16"><path d="M1 3h14v10H1zM2 4l6 5 6-5v1L8 10 2 5z"/></svg>info@halvorsenlawgrp.com</li>
      <li><svg viewBox="0 0 16 16"><path d="M8 1a7 7 0 1 0 0 14A7 7 0 0 0 8 1zm0 1.5c.8 1 1.4 2.7 1.5 4.5h-3C6.6 5.2 7.2 3.5 8 2.5zM2.6 7h2.4c.1-1.6.5-3 1.1-4.1A5.5 5.5 0 0 0 2.6 7zm8.4 0h2.4a5.5 5.5 0 0 0-3.5-4.1c.6 1.1 1 2.5 1.1 4.1zM2.6 9a5.5 5.5 0 0 0 3.5 4.1C5.5 12 5.1 10.6 5 9zm3.9 0c.1 1.8.7 3.5 1.5 4.5.8-1 1.4-2.7 1.5-4.5zm4.5 0c-.1 1.6-.5 3-1.1 4.1A5.5 5.5 0 0 0 13.4 9z"/></svg>www.halvorsenlawgrp.com</li>
    </ul>

    <div class="badge" role="img" aria-label="CPRS certification badge"></div>

    <div class="signature">
      <p class="signature__name">Trevor J. Halvorsen</p>
      <p class="signature__title">Board Certified Civil Trial Specialist</p>
    </div>
  </section>

  <section class="card card--back" aria-label="Business card, blue side">
    <div class="brand">
      <span class="brand__mark"></span>
      <span class="brand__name">Halvorsen Law</span>
    </div>
    <div class="practice">
      <p>Personal Injury | Criminal Law</p>
      <p>Former Insurance Company Attorney | Former Criminal Prosecutor</p>
    </div>
  </section>

</body>
</html>
```